Brimble Diecast Torvel Collectables Website

looking for a vibrant web site marketplace built for diecast car enthusiasts to buy, sell, and trade with ease. Whether you're looking to showcase your own collection or discover rare and exciting models, our site makes the process simple and enjoyable. Clients can browse a curated inventory of high‑quality diecast cars, connect with fellow collectors, and find the perfect pieces to expand their collection. With a smooth user experience and a community-driven spirit, we’re the go‑to destination for anyone passionate about diecast cars.

Target Market(s)

diecast collectors

Industry/Entity Type

Diecast Collectables

Coding

Coded - Design and coding required

Number of Pages Required

3 page

Font styles to use
Sans Serif

Colors
EE7325
F08F49
F5BC92
FAE3D3
FDF4ED

Requirements
Must have
• Cool look and feel. Woo commerce page to post and sell my inventory
Nice to have
• page for users to post their cars or looking for trades.
Should not have
• look cheap

```html
<!DOCTYPE html>
<html lang="en">
<head>
<meta charset="utf-8">
<title>Brimble Diecast — Buy. Sell. Trade. Collect.</title>
<link href="https://fonts.googleapis.com/css2?family=Plus+Jakarta+Sans:wght@500;600;700;800&family=Inter:wght@400;500;600&display=swap" rel="stylesheet">
<style>
:root{
  --brand:#c0581c;
  --brand-dark:#a94a15;
  --orange:#EE7325;
  --orange-2:#F08F49;
  --peach:#F5BC92;
  --peach-soft:#FAE3D3;
  --cream:#FDF4ED;
  --ink:#1d1714;
  --text:#4d4541;
  --muted:#8a807a;
  --line:#ece4de;
  --white:#ffffff;
  --footer:#f6f4f3;
}
*{box-sizing:border-box;margin:0;padding:0}
html,body{width:1200px;height:5085px;overflow:hidden}
body{font-family:"Inter",sans-serif;color:var(--ink);background:var(--white);position:relative}
h1,h2,h3,h4,.display{font-family:"Plus Jakarta Sans",sans-serif}
a{color:inherit;text-decoration:none}
.abs{position:absolute}

/* nav */
.nav{position:absolute;left:0;top:0;width:1200px;height:98px;background:#fdf6f1;display:flex;align-items:center;padding:0 40px}
.brand{display:flex;align-items:center;gap:10px;font-family:"Plus Jakarta Sans",sans-serif;font-weight:800;font-size:13px;color:var(--brand)}
.brand-dot{width:46px;height:46px;border-radius:50%;background:var(--brand)}
.nav-links{display:flex;gap:30px;margin-left:40px;font-size:14px;color:#3a322e}
.nav-links a:first-child{font-weight:600;color:var(--ink)}
.search{position:absolute;left:705px;top:26px;width:236px;height:44px;border-radius:22px;background:#faeee4;display:flex;align-items:center;padding-left:16px;gap:12px;font-size:12px;color:#b7a9a0}
.nav-icon{position:absolute;top:38px}
.btn-nav{position:absolute;left:1040px;top:34px;width:126px;height:30px;border-radius:15px;background:var(--brand);color:#fff;font-size:12px;font-weight:600;display:flex;align-items:center;justify-content:center}

/* hero */
.hero-title{position:absolute;left:67px;top:244px;font-size:60px;line-height:64px;font-weight:700;letter-spacing:-1.5px}
.hero-title span{color:var(--brand)}
.hero-copy{position:absolute;left:67px;top:460px;width:530px;font-size:15px;line-height:26px;color:var(--text)}
.btn{display:inline-flex;align-items:center;justify-content:center;border-radius:30px;font-weight:600;font-size:15px}
.btn-primary{background:var(--brand);color:#fff;box-shadow:0 8px 18px rgba(192,88,28,.25)}
.btn-ghost{background:#fff;border:1px solid var(--line);color:var(--ink)}
.feature-card{position:absolute;left:632px;top:180px;width:488px;height:512px;background:#fff;border-radius:16px;box-shadow:0 18px 40px rgba(0,0,0,.1);transform:rotate(2deg);overflow:hidden}
.feature-card .media{height:320px;background:linear-gradient(180deg,#f6f6f6,#e6e4e2);}
.feature-info{position:absolute;left:16px;right:24px;top:350px;height:130px;background:#fff;border-radius:12px;box-shadow:0 6px 16px rgba(0,0,0,.08);transform:rotate(-2deg);padding:22px 24px}
.eyebrow{font-size:11px;letter-spacing:2px;text-transform:uppercase;color:var(--brand);font-weight:600}
.feature-info h3{font-size:22px;font-weight:600;margin-top:8px}
.feature-info .meta{position:absolute;left:24px;bottom:26px;font-size:12px;color:var(--text)}
.feature-info .price{position:absolute;right:24px;bottom:20px;font-size:18px;font-weight:700}

/* band */
.band{position:absolute;left:8px;width:1184px;background:#fdefe4}
.section-title{text-align:center;font-size:38px;font-weight:700;line-height:50px;letter-spacing:-.5px}
.underline{display:inline-block;border-bottom:4px solid var(--brand);padding-bottom:2px}
.pillar{position:absolute;width:310px;text-align:center}
.pillar .ico{width:58px;height:58px;border-radius:50%;background:#fbdcc7;margin:0 auto;display:flex;align-items:center;justify-content:center}
.pillar h3{font-size:17px;font-weight:600;margin-top:38px}
.pillar p{font-size:13.5px;line-height:25px;color:var(--text);margin-top:22px}

/* featured */
.feat-head{position:absolute;left:97px;top:1430px}
.feat-head h2{font-size:40px;font-weight:700;letter-spacing:-.8px}
.feat-head p{font-size:14px;line-height:24px;color:var(--text);width:470px;margin-top:10px}
.gallery-link{position:absolute;left:948px;top:1510px;font-size:14px;font-weight:600;color:var(--brand);display:flex;align-items:center;gap:8px}
.hero-model{position:absolute;left:97px;top:1580px;width:665px;height:552px;border-radius:16px;overflow:hidden;background:radial-gradient(ellipse at 50% 55%,#2d6fb8 0%,#1f4f8c 28%,#5c5f64 60%,#3d3f43 100%)}
.hero-model .overlay{position:absolute;left:0;right:0;bottom:0;height:178px;background:rgba(70,70,74,.78);padding:42px 30px}
.badge{display:inline-block;background:var(--brand);color:#fff;font-size:11px;font-weight:700;letter-spacing:1.5px;padding:4px 10px;border-radius:4px}
.hero-model h3{color:#fff;font-size:26px;font-weight:600;margin-top:10px}
.hero-model .meta{color:#d6d2cf;font-size:12.5px;line-height:22px;width:290px;margin-top:6px}
.hero-model .price{position:absolute;right:30px;top:52px;color:#fff;font-family:"Plus Jakarta Sans",sans-serif;font-size:34px;font-weight:600}
.hero-model .bid{position:absolute;right:30px;top:104px;width:102px;height:32px;border-radius:16px;background:#fff;font-size:12px;font-weight:600;display:flex;align-items:center;justify-content:center}
.mini{position:absolute;left:787px;width:321px;height:257px;background:#fff;border-radius:14px;box-shadow:0 8px 24px rgba(0,0,0,.08);padding:22px}
.mini .media{height:148px;border-radius:8px}
.mini h4{font-size:19px;font-weight:600;margin-top:20px}
.mini .scale{font-size:12px;color:var(--muted);margin-top:6px}
.mini .price{position:absolute;right:22px;bottom:24px;font-size:20px;font-weight:700;color:var(--brand);font-family:"Plus Jakarta Sans",sans-serif}

/* steps */
.step{position:absolute;top:2360px;width:316px;height:340px;background:#fff;border-radius:14px;box-shadow:0 8px 24px rgba(200,120,70,.08);padding:34px 38px}
.step .num{position:absolute;right:22px;top:6px;font-family:"Plus Jakarta Sans",sans-serif;font-size:60px;font-weight:800;color:#f1ebe7}
.step h3{font-size:22px;font-weight:600;margin-top:36px}
.step p{font-size:13.5px;line-height:25px;color:var(--text);margin-top:20px}
.step .link{position:absolute;left:50px;bottom:38px;font-size:14px;font-weight:600;color:var(--brand);display:flex;gap:14px;align-items:center}

/* community */
.portrait{position:absolute;border-radius:12px}
.comm{position:absolute;left:623px;top:2906px;width:470px}
.comm h2{font-size:40px;line-height:45px;font-weight:700;margin-top:14px;letter-spacing:-.8px}
.comm .lead{font-size:15px;line-height:27px;color:var(--text);margin-top:28px}
.perk{display:flex;gap:14px;margin-top:22px}
.perk h4{font-size:19px;font-weight:600}
.perk p{font-size:12px;line-height:19px;color:var(--muted);margin-top:6px}
.btn-join{display:flex;align-items:center;justify-content:center;width:200px;height:48px;border-radius:24px;background:var(--orange);color:#fff;font-weight:600;font-size:14px;margin-top:26px}

/* trust */
.trust-sub{position:absolute;left:300px;width:600px;text-align:center;top:3700px;font-size:15px;line-height:28px;color:var(--text)}
.trust{position:absolute;top:3818px;width:232px;height:188px;background:#fdf4ed;border-radius:12px;text-align:center;padding:26px 20px;box-shadow:0 4px 14px rgba(200,120,70,.06)}
.trust h4{font-size:19px;line-height:22px;font-weight:600;margin-top:12px}
.trust p{font-size:12px;line-height:18px;color:var(--muted);margin-top:12px}

/* cta */
.cta{position:absolute;left:97px;top:4130px;width:1011px;height:468px;border-radius:24px;background:radial-gradient(ellipse at 85% 95%,#fbe6d8 0%,rgba(251,230,216,0) 42%),linear-gradient(110deg,#f29a5e 0%,#ee7a32 35%,#ee7325 70%,#f08f49 100%);text-align:center;box-shadow:0 16px 40px rgba(238,115,37,.25)}
.cta h2{color:#fff;font-size:56px;line-height:58px;font-weight:700;margin-top:84px;letter-spacing:-1px}
.cta p{color:#fff;font-size:16px;line-height:26px;width:560px;margin:28px auto 0;opacity:.95}
.cta .actions{display:flex;gap:16px;justify-content:center;margin-top:40px}
.cta .btn{height:62px;width:165px;font-size:15px}
.btn-white{background:#fff;color:var(--brand)}
.btn-dark{background:#c0581f;color:#fff}

/* footer */
.footer{position:absolute;left:0;top:4629px;width:1200px;height:456px;background:var(--footer)}
.footer .about{position:absolute;left:38px;top:155px;width:240px;font-size:13px;line-height:24px;color:var(--muted)}
.social{position:absolute;top:288px;display:flex;gap:14px;left:38px}
.social span{width:32px;height:32px;border-radius:50%;background:#fff;border:1px solid var(--line);display:flex;align-items:center;justify-content:center}
.fcol{position:absolute;top:76px}
.fcol h5{font-family:"Plus Jakarta Sans",sans-serif;font-size:13px;font-weight:600;margin-bottom:26px}
.fcol a{display:block;font-size:13px;color:var(--muted);margin-bottom:19px}
.fcol p{font-size:12px;line-height:18px;color:var(--muted);width:220px}
.email{margin-top:18px;width:220px;height:38px;border-radius:19px;background:#fff;border:1px solid var(--line);font-size:12px;color:var(--muted);display:flex;align-items:center;padding-left:16px}
.go{position:absolute;left:226px;top:104px;width:24px;height:24px;border-radius:50%;background:var(--brand);display:flex;align-items:center;justify-content:center}
.footer .rule{position:absolute;left:38px;right:38px;top:370px;border-top:1px solid var(--line)}
.copy{position:absolute;left:38px;top:392px;font-size:11.5px;color:var(--muted)}
.cities{position:absolute;right:38px;top:392px;font-size:10.5px;letter-spacing:2px;color:var(--muted);display:flex;gap:30px}
</style>
</head>
<body>

<header class="nav">
  <div class="brand"><span class="brand-dot"></span></div>
  <nav class="nav-links"><a>Marketplace</a><a>Sell &amp; Trade</a><a>Community</a></nav>
  <div class="search">
    <svg width="12" height="12" viewBox="0 0 24 24" fill="none" stroke="#b07a55" stroke-width="3"><circle cx="10" cy="10" r="7"/><path d="M15 15l6 6"/></svg>
    Search models...
  </div>
  <svg class="nav-icon" style="left:964px" width="18" height="20" viewBox="0 0 18 20" fill="none" stroke="#1d1714" stroke-width="2"><rect x="2" y="6" width="14" height="13" rx="1.5"/><path d="M6 6V4a3 3 0 016 0v2"/></svg>
  <svg class="nav-icon" style="left:1000px" width="18" height="18" viewBox="0 0 18 18" fill="none" stroke="#1d1714" stroke-width="2"><circle cx="9" cy="5" r="4"/><path d="M1 17c1-4 4-6 8-6s7 2 8 6"/></svg>
  <a class="btn-nav">List Your Car</a>
</header>

<section class="hero">
  <h1 class="hero-title">Buy. Sell. Trade.<br>Collect. — <span>All</span><br><span>in One Place</span></h1>
  <p class="hero-copy">Discover rare diecast cars from world-class collectors. A curated marketplace where precision engineering meets the passion of the hunt.</p>
  <a class="btn btn-primary abs" style="left:67px;top:575px;width:230px;height:58px">Browse Collection</a>
  <a class="btn btn-ghost abs" style="left:313px;top:575px;width:172px;height:58px">List Your Car</a>
  <article class="feature-card">
    <div class="media" role="img" aria-label="Red classic sports car diecast model on a white reflective surface"></div>
    <div class="feature-info">
      <div class="eyebrow">Featured Arrival</div>
      <h3>1967 GT Fastback</h3>
      <div class="meta">Scale: 1:18 | Limited Edition</div>
      <div class="price">$285.00</div>
    </div>
  </article>
</section>

<section class="band" style="top:815px;height:508px">
  <h2 class="section-title" style="margin-top:74px">Where Collectors Connect &amp;<br><span class="underline">Collections Grow</span></h2>
  <div class="pillar" style="left:92px;top:228px">
    <div class="ico"><svg width="24" height="24" viewBox="0 0 24 24" fill="none" stroke="#c0581c" stroke-width="2"><circle cx="12" cy="12" r="9"/><path d="M8 12l3 3 5-6"/></svg></div>
    <h3>Curated Inventory</h3>
    <p>Every listing is hand-reviewed to ensure authenticity and quality standards are met before going live.</p>
  </div>
  <div class="pillar" style="left:445px;top:228px">
    <div class="ico"><svg width="24" height="24" viewBox="0 0 24 24" fill="none" stroke="#c0581c" stroke-width="2"><path d="M4 9h15l-4-4M20 15H5l4 4"/></svg></div>
    <h3>Seamless Trading</h3>
    <p>Our proprietary secure trade system allows enthusiasts to swap models with verified protection and low fees.</p>
  </div>
  <div class="pillar" style="left:797px;top:228px">
    <div class="ico"><svg width="26" height="20" viewBox="0 0 26 20" fill="#c0581c"><circle cx="13" cy="5" r="4"/><circle cx="5" cy="7" r="3"/><circle cx="21" cy="7" r="3"/><path d="M6 18c0-4 3-7 7-7s7 3 7 7zM0 18c0-3 2-6 5-6 1 0 2 0 2 1-2 1-3 3-3 5zM26 18c0-3-2-6-5-6-1 0-2 0-2 1 2 1 3 3 3 5z"/></svg></div>
    <h3>Collector Community</h3>
    <p>Join specialized forums and local groups. Share your display setups and find the next piece for your garage.</p>
  </div>
</section>

<section class="featured">
  <div class="feat-head">
    <h2>Featured Diecast Models</h2>
    <p>The pinnacle of miniature engineering. Explore our most sought-after listings of the week.</p>
  </div>
  <a class="gallery-link">View Entire Gallery <svg width="16" height="12" viewBox="0 0 16 12" fill="none" stroke="#c0581c" stroke-width="2"><path d="M1 6h13M9 1l5 5-5 5"/></svg></a>
  <article class="hero-model" role="img" aria-label="Blue sports coupe diecast model, front view, on a dark studio background">
    <div class="overlay">
      <span class="badge">RARE FIND</span>
      <h3>Apex RS ‘Shark Blue’</h3>
      <div class="meta">Scale 1:12 | Signature Edition | Mint Condition</div>
      <div class="price">$1,250</div>
      <a class="bid">Place Bid</a>
    </div>
  </article>
  <article class="mini" style="top:1580px">
    <div class="media" role="img" aria-label="Dark red classic muscle car diecast model" style="background:linear-gradient(180deg,#f1f0ef,#d9d6d4)"></div>
    <h4>Classic Corsa 1965</h4>
    <div class="scale">1:24 Scale</div>
    <div class="price">$1,045</div>
  </article>
  <article class="mini" style="top:1865px">
    <div class="media" role="img" aria-label="Silver concept hypercar diecast model" style="background:linear-gradient(180deg,#9a9b9e,#4a4b4f)"></div>
    <h4>Concept Vela 2023</h4>
    <div class="scale">1:18 Scale</div>
    <div class="price">$310</div>
  </article>
</section>

<section class="band" style="top:2270px;height:523px"></section>
<article class="step" style="left:97px">
  <span class="num">01</span>
  <svg width="34" height="38" viewBox="0 0 34 38" fill="#c0581c"><path d="M10 12V9a7 7 0 0114 0v3h-3V9a4 4 0 00-8 0v3z"/><rect x="1" y="12" width="32" height="26" rx="3"/></svg>
  <h3>Buy Your Grail</h3>
  <p>Access an exclusive global marketplace of verified miniature masterpieces. Browse by scale, brand, or era.</p>
  <a class="link">Start Shopping <svg width="16" height="12" viewBox="0 0 16 12" fill="none" stroke="#c0581c" stroke-width="2"><path d="M1 6h13M9 1l5 5-5 5"/></svg></a>
</article>
<article class="step" style="left:445px">
  <span class="num">02</span>
  <svg width="38" height="38" viewBox="0 0 38 38" fill="#c0581c"><path d="M2 4a2 2 0 012-2h14l18 18-16 16L2 18z"/><circle cx="10" cy="10" r="3" fill="#fff"/></svg>
  <h3>Sell with Ease</h3>
  <p>Turn your collection into capital. Reach thousands of serious collectors with our professional listing tools.</p>
  <a class="link">List a Model <svg width="16" height="12" viewBox="0 0 16 12" fill="none" stroke="#c0581c" stroke-width="2"><path d="M1 6h13M9 1l5 5-5 5"/></svg></a>
</article>
<article class="step" style="left:792px">
  <span class="num">03</span>
  <svg width="40" height="40" viewBox="0 0 40 40" fill="none" stroke="#c0581c" stroke-width="3.5"><path d="M8 18a12 12 0 0121-8l3 3M32 22a12 12 0 01-21 8l-3-3"/><path d="M32 5v8h-8M8 35v-8h8"/><path d="M15 20l4 4 6-7"/></svg>
  <h3>Trade &amp; Swap</h3>
  <p>Trade up or pivot your focus. Securely swap models with other enthusiasts using our escrow protection.</p>
  <a class="link">Explore Trades <svg width="16" height="12" viewBox="0 0 16 12" fill="none" stroke="#c0581c" stroke-width="2"><path d="M1 6h13M9 1l5 5-5 5"/></svg></a>
</article>

<section class="community">
  <div class="portrait" role="img" aria-label="Portrait of a collector in a dark jacket" style="left:97px;top:2977px;width:235px;height:238px;background:linear-gradient(160deg,#6a5a4c,#2a2420)"></div>
  <div class="portrait" role="img" aria-label="Portrait of a collector in a dark suit" style="left:97px;top:3230px;width:235px;height:180px;background:linear-gradient(160deg,#3a3a3c,#141416)"></div>
  <div class="portrait" role="img" aria-label="Portrait of a bearded collector in a suit" style="left:347px;top:2932px;width:235px;height:233px;background:linear-gradient(160deg,#2e2e30,#151516)"></div>
  <div class="portrait" role="img" aria-label="Portrait of a collector wearing glasses and a red tie" style="left:347px;top:3180px;width:235px;height:187px;background:linear-gradient(160deg,#5a4a3e,#1e1a18)"></div>
  <div class="comm">
    <div class="eyebrow">The Collective</div>
    <h2>More Than a<br>Marketplace — A<br>Community</h2>
    <p class="lead">Brimble Diecast is built by collectors, for collectors. Join 50,000+ enthusiasts who share detailed photography, host virtual garage tours, and meet up for exclusive events.</p>
    <div class="perk">
      <svg width="20" height="18" viewBox="0 0 20 18" fill="none" stroke="#c0581c" stroke-width="2"><path d="M2 2h13v9H7l-4 3v-3H2z"/><path d="M17 6h1v9h-1v3l-4-3H9"/></svg>
      <div><h4>Expert Forums</h4><p>Get advice on restoration, valuation, and spotting replicas.</p></div>
    </div>
    <div class="perk">
      <svg width="20" height="20" viewBox="0 0 20 20" fill="none" stroke="#c0581c" stroke-width="2"><circle cx="10" cy="10" r="8"/><path d="M10 5l1.5 3 3.5.5-2.5 2.5.5 3.5-3-1.7-3 1.7.5-3.5L5 8.5 8.5 8z" fill="#c0581c" stroke="none"/></svg>
      <div><h4>Photo Showcases</h4><p>Upload your professional dioramas and gain community recognition.</p></div>
    </div>
    <a class="btn-join">Join the Community</a>
  </div>
</section>

<section class="band" style="top:3553px;height:577px">
  <h2 class="section-title" style="margin-top:80px">Built on Trust &amp; Quality</h2>
</section>
<p class="trust-sub">We maintain the highest standards in the industry to ensure your peace of mind with every transaction.</p>
<article class="trust" style="left:97px">
  <svg width="34" height="30" viewBox="0 0 34 30" fill="none" stroke="#c0581c" stroke-width="2.5"><rect x="2" y="7" width="30" height="21" rx="2"/><path d="M11 7l2-5h8l2 5"/><circle cx="17" cy="17" r="5"/></svg>
  <h4>High-Res<br>Standards</h4><p>Mandatory 360° views for all premium listings.</p>
</article>
<article class="trust" style="left:357px">
  <svg width="28" height="32" viewBox="0 0 28 32" fill="none" stroke="#c0581c" stroke-width="2.5"><path d="M14 2l11 4v9c0 8-5 13-11 15C8 28 3 23 3 15V6z"/></svg>
  <h4>Verified Sellers</h4><p>Background checked and rating-verified community.</p>
</article>
<article class="trust" style="left:618px">
  <svg width="32" height="32" viewBox="0 0 32 32" fill="none" stroke="#c0581c" stroke-width="2.5"><rect x="3" y="3" width="26" height="26" rx="2"/><path d="M3 11h26M12 17h8"/></svg>
  <h4>Condition<br>Grading</h4><p>Standardized grading system for objective condition reports.</p>
</article>
<article class="trust" style="left:877px">
  <svg width="34" height="28" viewBox="0 0 34 28" fill="none" stroke="#c0581c" stroke-width="2.5"><rect x="2" y="2" width="30" height="18" rx="2"/><circle cx="17" cy="11" r="4" fill="#c0581c"/><path d="M4 25h26"/></svg>
  <h4>Escrow<br>Protection</h4><p>Funds are only released once you've inspected the model.</p>
</article>

<section class="cta">
  <h2>Start Building Your Dream<br>Collection Today</h2>
  <p>Join the world’s most sophisticated diecast marketplace and find that missing piece.</p>
  <div class="actions">
    <a class="btn btn-white">Get Started Now</a>
    <a class="btn btn-dark">Learn More</a>
  </div>
</section>

<footer class="footer">
  <div class="brand abs" style="left:38px;top:62px"><span class="brand-dot" style="width:50px;height:50px"></span><span>Brimble Diecast</span></div>
  <p class="about">Your Marketplace for Miniature Masterpieces. Connecting collectors across the globe since 2024.</p>
  <div class="social">
    <span><svg width="12" height="12" viewBox="0 0 12 12" fill="none" stroke="#1d1714" stroke-width="1.5"><circle cx="2.5" cy="6" r="1.5"/><circle cx="9.5" cy="2.5" r="1.5"/><circle cx="9.5" cy="9.5" r="1.5"/><path d="M4 5.2l4-2M4 6.8l4 2"/></svg></span>
    <span><svg width="12" height="12" viewBox="0 0 12 12" fill="#1d1714"><circle cx="3" cy="4" r="1.5"/><circle cx="6" cy="3.5" r="1.5"/><circle cx="9" cy="4" r="1.5"/><rect x="1" y="7" width="10" height="3" rx="1.5"/></svg></span>
    <span><svg width="12" height="12" viewBox="0 0 12 12" fill="none" stroke="#1d1714" stroke-width="1.5"><rect x="1" y="3" width="7" height="6" rx="1"/><path d="M8 5l3-2v6l-3-2"/></svg></span>
  </div>
  <div class="fcol" style="left:330px">
    <h5>Quick Links</h5>
    <a>Browse Collection</a><a>Sell Your Cars</a><a>Trade Portal</a><a>Community Forum</a><a>Newsletter</a>
  </div>
  <div class="fcol" style="left:625px">
    <h5>Resources</h5>
    <a>FAQ</a><a>Contact Support</a><a>Terms of Service</a><a>Privacy Policy</a><a>Grading Guide</a>
  </div>
  <div class="fcol" style="left:918px">
    <h5>Join the Mailing List</h5>
    <p>Receive weekly rare find alerts and community auction highlights.</p>
    <div class="email">email@address.com</div>
    <span class="go"><svg width="10" height="10" viewBox="0 0 10 10" fill="none" stroke="#fff" stroke-width="2"><path d="M3 1l4 4-4 4"/></svg></span>
  </div>
  <div class="rule"></div>
  <div class="copy">© 2026 Brimble Diecast. Your Marketplace for Miniature Masterpieces.</div>
  <div class="cities"><span>LONDON</span><span>•</span><span>TOKYO</span><span>•</span><span>NEW YORK</span></div>
</footer>

</body>
</html>
```